Business Card / Appointment Card for Physician

On one side it should give the logo, address, and contact information, and on the other side it should br an Appointment card.

One Side:
Logo (see attached files)
Board Certified American Orthopedic Surgery

1487 Harrowgate Ave.
Suite KM7
Bronx, NY 10527
Tel: (718) 552 - 1948
Fax: (718) 552 - 7210

628 Fourth Ave.
Suite 42
New York, NY 10087
Tel: (212) 734 - 2815

Second Side:
Appointment
give them a choice of Bronx or Mahattan office
For:
Date:
Time:

If you are unable to keep your appointment, please call (718) 263-5102 24hrs in advance.

Target Market(s)

People that need orthopedic surgery

Industry/Entity Type

Business

Contact Information for Business Card

smart and attractive

Requirements
Must have
• logo
• contact information on one side, appointment information on the other

```html
<!DOCTYPE html>
<html lang="en">
<head>
<meta charset="utf-8">
<title>Daniel R. Whitford MD PC – Business &amp; Appointment Card</title>
<link href="https://fonts.googleapis.com/css2?family=Mulish:wght@500&family=Open+Sans:ital,wght@0,400;0,700;1,400&family=Roboto:wght@400&display=swap" rel="stylesheet">
<style>
  :root {
    --page-bg: #e6e6e6;
    --card-bg: #f7f7f7;
    --brand-blue: #0a63a3;
    --brand-green: #6aa83b;
    --text-grey: #4a4a4a;
    --leader-grey: #7a7a7a;
    --badge-green: #2f6b4a;
    --faint-mark: rgba(10, 99, 163, 0.07);
  }
  * { box-sizing: border-box; margin: 0; padding: 0; }
  html, body { width: 1200px; height: 960px; overflow: hidden; }
  body { background: var(--page-bg); position: relative; font-family: "Roboto", sans-serif; }

  .card { position: absolute; width: 600px; height: 342px; background: var(--card-bg); overflow: hidden; }
  .card--front { left: 314px; top: 113px; }
  .card--back { left: 311px; top: 472px; }

  /* Front */
  .brand-band { position: absolute; left: 0; top: 36px; width: 100%; height: 62px; background: var(--brand-blue); }
  .brand-dot { position: absolute; left: 269px; top: 2px; width: 58px; height: 58px; border-radius: 50%; background: #fff; border: 3px solid var(--brand-blue); }
  .practice-name { position: absolute; top: 100px; width: 100%; text-align: center; font-family: "Mulish", sans-serif; font-weight: 500; font-size: 20px; letter-spacing: .3px; color: var(--brand-blue); }
  .practice-tagline { position: absolute; top: 123px; width: 100%; text-align: center; font-family: "Mulish", sans-serif; font-weight: 500; font-size: 10.5px; color: var(--brand-blue); }
  .practice-tagline .amp { color: var(--brand-green); }

  .certification { position: absolute; left: 231px; top: 147px; display: flex; align-items: center; gap: 6px; }
  .certification__seal { width: 44px; height: 50px; border-radius: 50%; background: var(--badge-green); border: 2px solid #c9c9c9; }
  .certification__label { font-family: "Roboto", sans-serif; font-size: 9px; line-height: 11px; color: #222; }

  .office { position: absolute; font-size: 15px; line-height: 18px; color: var(--text-grey); }
  .office--bronx { left: 32px; top: 217px; }
  .office--manhattan { right: 31px; top: 236px; text-align: right; }
  .contact-line { display: flex; align-items: center; gap: 8px; margin-top: 2px; }
  .office--bronx .contact-line:first-of-type { margin-top: 6px; }
  .office--manhattan .contact-line { justify-content: flex-end; margin-top: 6px; }
  .contact-line svg { width: 14px; height: 14px; fill: var(--brand-blue); }

  /* Back */
  .faint-mark { position: absolute; left: 140px; top: 112px; width: 160px; height: 160px; border-radius: 50%; background: var(--faint-mark); }
  .appt-title { position: absolute; top: 28px; width: 100%; text-align: center; font-family: "Open Sans", sans-serif; font-weight: 700; font-size: 24px; color: var(--brand-blue); }
  .appt-subtitle { position: absolute; top: 59px; width: 100%; text-align: center; font-family: "Open Sans", sans-serif; font-size: 12.5px; color: var(--text-grey); }

  .appt-field { position: absolute; left: 35px; width: 532px; display: flex; align-items: baseline; font-family: "Open Sans", sans-serif; font-size: 14px; color: var(--brand-blue); }
  .leader { flex: 1; border-bottom: 2px dotted var(--leader-grey); margin-left: 4px; height: 1px; transform: translateY(-3px); }
  .field-for { top: 98px; }
  .field-date { top: 141px; }
  .field-date .label-time { margin-left: 6px; }
  .field-date .ampm { font-size: 12px; margin-left: 6px; }
  .field-note { top: 226px; }
  .field-extra { top: 258px; }

  .weekdays { position: absolute; top: 187px; left: 64px; display: flex; gap: 0; font-family: "Open Sans", sans-serif; font-size: 14px; color: var(--brand-blue); }
  .weekday { display: flex; align-items: center; gap: 4px; margin-right: 21px; }
  .weekday:last-child { margin-right: 0; }
  .tickbox { width: 17px; height: 14px; border: 1.2px solid #555; background: #fff; }

  .appt-notice { position: absolute; top: 293px; width: 100%; text-align: center; font-family: "Open Sans", sans-serif; font-style: italic; font-size: 12.5px; color: var(--text-grey); }
</style>
</head>
<body>

<section class="card card--front" aria-label="Business card front">
  <div class="brand-band"><div class="brand-dot"></div></div>
  <h1 class="practice-name">DANIEL R. WHITFORD MD PC</h1>
  <p class="practice-tagline">ORTHOPAEDIC SURGERY <span class="amp">&amp;</span> SPORTS MEDICINE</p>

  <div class="certification">
    <div class="certification__seal" aria-hidden="true"></div>
    <p class="certification__label">The National Council<br>of Bone &amp; Joint Care</p>
  </div>

  <address class="office office--bronx" style="font-style:normal">
    1487 Harrowgate Ave.<br>
    Suite KM7<br>
    Bronx, NY 10527
    <div class="contact-line">
      <svg viewBox="0 0 24 24" aria-label="Telephone"><path d="M6.6 10.8a15.1 15.1 0 0 0 6.6 6.6l2.2-2.2c.3-.3.7-.4 1-.2 1.1.4 2.3.6 3.6.6.6 0 1 .4 1 1V20c0 .6-.4 1-1 1A17 17 0 0 1 3 4c0-.6.4-1 1-1h3.5c.6 0 1 .4 1 1 0 1.3.2 2.5.6 3.6.1.3 0 .7-.2 1z"/></svg>
      (718) 552 - 1948
    </div>
    <div class="contact-line">
      <svg viewBox="0 0 24 24" aria-label="Fax"><path d="M6 3h9l3 3v4H6zM3 11h18v9H3zm3 3v2h5v-2zm9 0v2h3v-2z"/></svg>
      (718) 552 - 7210
    </div>
  </address>

  <address class="office office--manhattan" style="font-style:normal">
    628 Fourth Ave.<br>
    Suite 42<br>
    New York, NY 10087
    <div class="contact-line">
      (212) 734 - 2815
      <svg viewBox="0 0 24 24" aria-label="Telephone"><path d="M17.4 10.8a15.1 15.1 0 0 1-6.6 6.6l-2.2-2.2c-.3-.3-.7-.4-1-.2-1.1.4-2.3.6-3.6.6-.6 0-1 .4-1 1V20c0 .6.4 1 1 1A17 17 0 0 0 21 4c0-.6-.4-1-1-1h-3.5c-.6 0-1 .4-1 1 0 1.3-.2 2.5-.6 3.6-.1.3 0 .7.2 1z"/></svg>
    </div>
  </address>
</section>

<section class="card card--back" aria-label="Appointment card">
  <div class="faint-mark" aria-hidden="true"></div>
  <h2 class="appt-title">APPOINTMENT</h2>
  <p class="appt-subtitle">GIVE THEM A CHOICE OF BRONX OR MAHATTAN OFFICE</p>

  <div class="appt-field field-for"><span>For:</span><span class="leader"></span></div>
  <div class="appt-field field-date">
    <span>Date:</span><span class="leader"></span>
    <span class="label-time">Time :</span><span class="leader" style="flex:0 0 136px"></span>
    <span class="ampm">AM/PM</span>
  </div>

  <div class="weekdays">
    <span class="weekday">Sun <span class="tickbox"></span></span>
    <span class="weekday">Mon <span class="tickbox"></span></span>
    <span class="weekday">Tue <span class="tickbox"></span></span>
    <span class="weekday">Wed <span class="tickbox"></span></span>
    <span class="weekday">Thu <span class="tickbox"></span></span>
    <span class="weekday">Fri <span class="tickbox"></span></span>
    <span class="weekday">Sat <span class="tickbox"></span></span>
  </div>

  <div class="appt-field field-note"><span>Note:</span><span class="leader"></span></div>
  <div class="appt-field field-extra"><span class="leader" style="margin-left:0"></span></div>

  <p class="appt-notice">If you are unable to keep your appointment, please call (718) 263-5102 24hrs in advance.</p>
</section>

</body>
</html>
```